Keglow Supply sales flyer for the licensed trade tri fold a4 leaflet style

Looking for a flyer / brochure to advertise our company service, needs to be modern and eye catching, aimed at licensee's and publicans. Our company saves them money on their beer losses.
I have attached some pictures which we use and our logo.
I have also attached leaflet that our parent company uses which contains more information.
Here are some key points
We are the originators of the specialist extended line cleaning service.
Our unique service allows for line cleaning to be extended from once every 7 days to once every 21 days.
We have provided our unique service since 1994
We guarantee our customers a minimum saving of 40% on their losses.
We are the only company to have been tested and proved by Tapwell and Brandt to improve quality and reduce costs.
Our web address is www.keglowsupplyuk.example if you need info.
Updates

Industry/Entity Type

It Company

Font styles to use
Sans Serif

Colors
fbee3d
ffffff
fece3e
fbed22
fbf289

Requirements
Must have
• We are the originators of the specialist extended line cleaning service.
• Our unique service allows for line cleaning to be extended from once every 7 days to once every 21 days.
• We have provided our unique service since 1994
• We guarantee our customers a minimum saving of 40% on their losses.
• We are the only company to have been tested and proved by Tapwell and Brandt to improve quality and reduce costs.

```html
<!DOCTYPE html>
<html lang="en">
<head>
<meta charset="UTF-8">
<title>Keglow Supply – Tri-fold Leaflet</title>
<link href="https://fonts.googleapis.com/css2?family=Poppins:wght@400;500;700&display=swap" rel="stylesheet">
<style>
  :root {
    --yellow: #fbee3d;
    --yellow-deep: #fbed22;
    --gold: #fece3e;
    --pale: #fbf289;
    --orange: #f2a818;
    --white: #ffffff;
    --paper: #f4f4f4;
    --ink: #1a1a1a;
    --stage: #e2e2e2;
  }
  * { box-sizing: border-box; margin: 0; padding: 0; }
  html, body { width: 1200px; height: 1200px; overflow: hidden; background: var(--stage); }
  body { font-family: "Poppins", sans-serif; color: var(--ink); position: relative; }

  .spread {
    position: absolute;
    left: 210px;
    width: 780px;
    height: 552px;
    display: flex;
    box-shadow: 0 6px 18px rgba(0,0,0,.18);
  }
  .spread--outside { top: 30px; }
  .spread--inside { top: 618px; }

  .panel { position: relative; width: 260px; height: 100%; overflow: hidden; }

  /* Outside: photo panel */
  .panel--bar-photo {
    background: linear-gradient(160deg, #3a2516 0%, #6b4a2a 30%, #c79a3a 55%, #e7c35a 70%, #5b3a20 100%);
  }
  .since-band {
    position: absolute; left: 0; right: 0; top: 70px;
    padding: 14px 18px;
    background: rgba(205,160,40,.72);
    color: var(--white);
    font-weight: 700; font-size: 17px; line-height: 1.3;
  }

  /* Outside: yellow middle panel */
  .panel--back { background: linear-gradient(180deg, var(--yellow) 0%, var(--yellow-deep) 60%, var(--gold) 100%); }
  .page-number { position: absolute; top: 18px; left: 18px; color: var(--white); font-weight: 700; font-size: 22px; }
  .web-curve { position: absolute; left: 0; bottom: 40px; width: 260px; height: 110px; }
  .web-address {
    position: absolute; left: 0; right: 0; bottom: 76px;
    font-size: 12.5px; font-weight: 700; text-align: center; transform: rotate(-10deg);
  }

  /* Outside: cover */
  .panel--cover { background: var(--paper); display: flex; align-items: flex-start; justify-content: center; }
  .brand { margin-top: 110px; display: flex; flex-direction: column; align-items: center; gap: 14px; }
  .brand__mark { width: 44px; height: 44px; border-radius: 50%; background: var(--gold); }
  .brand__name { font-weight: 500; font-size: 24px; color: #3a1e12; text-align: center; line-height: 1.2; }

  /* Inside: droplets panel */
  .panel--droplets {
    background: radial-gradient(circle at 30% 20%, var(--pale) 0%, var(--yellow) 35%, var(--yellow-deep) 65%, var(--gold) 100%);
  }
  .headline {
    position: absolute; left: 26px; right: 16px; top: 250px;
    font-weight: 700; font-size: 27px; line-height: 1.18; color: var(--ink);
  }
  .headline mark { background: var(--white); color: var(--ink); padding: 0 4px; }

  /* Inside: centre panel */
  .panel--service { background: var(--white); }
  .arc { position: absolute; left: 0; width: 260px; height: 40px; }
  .arc--top { top: 0; }
  .arc--bottom { bottom: 0; }
  .service-box {
    position: absolute; left: 28px; right: 28px; top: 58px; height: 270px;
    background: var(--yellow);
    padding: 26px 18px;
    text-align: center; font-size: 13px; line-height: 1.35;
    display: flex; flex-direction: column; justify-content: space-between;
  }
  .service-box p + p { font-weight: 500; }
  .glasses-photo {
    position: absolute; left: 28px; right: 28px; top: 346px; height: 130px;
    background: linear-gradient(90deg, #f7c52a 0%, #fbe27a 50%, #f1f1f1 100%);
    border-radius: 4px;
  }

  /* Inside: proof panel */
  .panel--proof { background: linear-gradient(160deg, #f6b62b 0%, var(--orange) 50%, #e89a12 100%); }
  .proof-photo {
    position: absolute; left: 60px; right: 60px; top: 20px; bottom: 20px;
    background: linear-gradient(180deg, rgba(255,240,200,.55) 0%, rgba(255,205,80,.45) 40%, rgba(255,190,40,.25) 100%);
    border-radius: 40px 40px 20px 20px;
  }
  .proof-frame {
    position: absolute; left: 36px; right: 36px; top: 96px; bottom: 96px;
    border: 2px solid var(--white);
    display: flex; align-items: center; padding: 20px;
  }
  .proof-frame p { font-size: 17px; line-height: 1.35; color: var(--ink); }
  .proof-frame strong { font-weight: 700; }
</style>
</head>
<body>

<section class="spread spread--outside">
  <div class="panel panel--bar-photo" role="img" aria-label="Photo of a pint glass of lager on a bar counter">
    <p class="since-band">We have provided our unique service since 1994</p>
  </div>

  <div class="panel panel--back">
    <span class="page-number">2</span>
    <svg class="web-curve" viewBox="0 0 260 110" preserveAspectRatio="none">
      <path d="M0 70 Q150 60 260 0 L260 30 Q150 90 0 110 Z" fill="#ffffff"/>
    </svg>
    <p class="web-address">www.keglowsupplyuk.example</p>
  </div>

  <div class="panel panel--cover">
    <div class="brand">
      <span class="brand__mark"></span>
      <span class="brand__name">Keglow Supply (UK)</span>
    </div>
  </div>
</section>

<section class="spread spread--inside">
  <div class="panel panel--droplets" role="img" aria-label="Close-up of condensation droplets on a cold glass of lager">
    <h1 class="headline">We are the <mark>originators</mark> of the specialist extended line cleaning service.</h1>
  </div>

  <div class="panel panel--service">
    <svg class="arc arc--top" viewBox="0 0 260 40" preserveAspectRatio="none">
      <path d="M0 30 Q130 5 260 12" stroke="#f2a818" stroke-width="6" fill="none"/>
    </svg>
    <div class="service-box">
      <p>Our unique service allows for line cleaning to be extended from once every 7 days to once every 21 days.</p>
      <p>We guarantee our customers a minimum saving of 40% on their losses.</p>
    </div>
    <div class="glasses-photo" role="img" aria-label="Three pint glasses: full, half full and empty"></div>
    <svg class="arc arc--bottom" viewBox="0 0 260 40" preserveAspectRatio="none">
      <path d="M0 32 Q130 10 260 8" stroke="#f2a818" stroke-width="6" fill="none"/>
    </svg>
  </div>

  <div class="panel panel--proof">
    <div class="proof-photo" role="img" aria-label="Large frosted pint glass of lager"></div>
    <div class="proof-frame">
      <p>We are the only company to have been tested and proved by Tapwell and Brandt to <strong>improve quality and reduce costs.</strong></p>
    </div>
  </div>
</section>

</body>
</html>
```